Lumo -Fresh business card design

It is a dry cleaning carpet business.
Red wine stain removal and pet urine treatments.
Servicing all regional areas.
Updates

all logo and pictures files have been uploaded

Industry/Entity Type

Dry Cleaning

Contact Information for Business Card

Lumo-Fresh Carpet and upholstery cleaning.
Servicing Albury/Wodonga and surrounding areas.
ph gus 0461273904 ,email lumofresh1@tealpost.example

Font styles to use
Serif
Sans Serif
Other font styles liked:
• lumo fresh logo font

Colors
ec2027
ffcf3e
33a6d7
0692cd

Requirements
Nice to have
• I have included photos of the logo and car and stripe on van ,I dont need all of them in the card just i would like to stick to these colours.

```html
<!DOCTYPE html>
<html lang="en">
<head>
<meta charset="utf-8">
<title>Lumo-Fresh Business Card</title>
<link href="https://fonts.googleapis.com/css2?family=Roboto+Condensed:wght@700&family=Questrial&display=swap" rel="stylesheet">
<style>
  :root {
    --red: #ec2027;
    --yellow: #ffe11a;
    --gold: #ffcf3e;
    --cyan: #2fe3f0;
    --blue: #0692cd;
    --sky: #33a6d7;
    --ink: #1a1a1a;
    --white: #ffffff;
  }
  html, body {
    margin: 0;
    padding: 0;
    width: 1200px;
    height: 740px;
    overflow: hidden;
    background: var(--white);
  }
  .card {
    position: relative;
    width: 1200px;
    height: 740px;
    overflow: hidden;
    background: var(--white);
    font-family: "Roboto Condensed", "Arial Narrow", sans-serif;
  }
  .card__backdrop {
    position: absolute;
    inset: 0;
  }
  .splash {
    position: absolute;
    border-radius: 50%;
  }
  .splash--top {
    left: 430px; top: -70px;
    width: 380px; height: 250px;
    background: radial-gradient(ellipse at center, rgba(236,32,39,0.85) 0%, rgba(236,32,39,0.5) 50%, rgba(236,32,39,0) 72%);
  }
  .splash--badge {
    left: 800px; top: 20px;
    width: 370px; height: 210px;
    background: radial-gradient(ellipse at center, var(--red) 0%, rgba(236,32,39,0.9) 48%, rgba(236,32,39,0) 72%);
  }
  .glass-art {
    position: absolute;
    left: -40px; top: 430px;
    width: 480px; height: 330px;
    border-radius: 0 60% 0 0;
    background: linear-gradient(160deg, #f2d7d8 0%, #e04a50 45%, #b0141b 100%);
    opacity: 0.9;
  }
  .slogan {
    position: absolute;
    left: 808px; top: 62px;
    display: flex;
    gap: 14px;
    align-items: flex-start;
  }
  .slogan__dot {
    width: 22px; height: 22px;
    margin-top: 10px;
    border-radius: 50%;
    background: var(--red);
    border: 3px solid var(--white);
    box-sizing: border-box;
  }
  .slogan__text {
    margin: 0;
    font-size: 47px;
    line-height: 54px;
    letter-spacing: 0.5px;
    color: var(--yellow);
    text-transform: uppercase;
    -webkit-text-stroke: 2px var(--ink);
    text-shadow: 3px 3px 0 var(--ink);
  }
  .brand {
    position: absolute;
    left: 73px; top: 196px;
    width: 640px;
  }
  .brand__name {
    margin: 0;
    font-size: 118px;
    line-height: 118px;
    color: var(--blue);
    letter-spacing: 1px;
  }
  .brand__rule {
    height: 5px;
    width: 610px;
    margin: 8px 0 10px 4px;
    background: linear-gradient(90deg, rgba(6,146,205,0), var(--blue) 35%, var(--blue) 65%, rgba(6,146,205,0));
  }
  .brand__tagline {
    margin: 0 0 0 58px;
    font-family: "Questrial", "Century Gothic", sans-serif;
    font-size: 38px;
    line-height: 44px;
    color: var(--ink);
    white-space: nowrap;
  }
  .area {
    position: absolute;
    right: 58px; top: 264px;
    margin: 0;
    text-align: right;
    color: var(--white);
    font-size: 37px;
    line-height: 55px;
    letter-spacing: 1px;
  }
  .contact {
    position: absolute;
    right: 58px;
    display: flex;
    align-items: center;
    gap: 12px;
    color: var(--white);
    font-size: 36px;
    letter-spacing: 0.5px;
    padding-bottom: 12px;
    border-bottom: 3px dashed var(--gold);
  }
  .contact--phone { top: 492px; padding-left: 8px; }
  .contact--email { top: 612px; font-size: 33px; }
  .contact__icon { flex: none; }
</style>
</head>
<body>
<main class="card">
  <svg class="card__backdrop" width="1200" height="740" viewBox="0 0 1200 740" aria-hidden="true">
    <path class="panel-cyan" d="M795 0 H1200 V740 H480 C470 700 460 660 470 610 C500 500 730 470 790 370 C850 260 830 150 795 0 Z" fill="var(--cyan)"/>
    <path class="swoosh swoosh--red" d="M765 -10 C800 150 822 262 762 362 C700 460 470 490 442 605 C428 660 440 700 450 750" fill="none" stroke="var(--red)" stroke-width="40"/>
    <path class="swoosh swoosh--yellow" d="M787 -10 C822 150 844 262 784 366 C722 466 492 496 464 610 C450 662 462 700 472 750" fill="none" stroke="var(--yellow)" stroke-width="8"/>
    <path class="swoosh swoosh--blue" d="M739 -10 C774 150 796 258 736 356 C674 452 444 484 416 600 C402 660 414 700 424 750" fill="none" stroke="var(--sky)" stroke-width="5"/>
  </svg>

  <div class="splash splash--top" role="img" aria-label="Red wine splash decoration"></div>
  <div class="splash splash--badge" role="img" aria-label="Red wine splash behind slogan"></div>
  <div class="glass-art" role="img" aria-label="Tilted glass of spilling red wine"></div>

  <div class="slogan">
    <span class="slogan__dot"></span>
    <p class="slogan__text">No soggy<br>wet carpets</p>
  </div>

  <header class="brand">
    <h1 class="brand__name">Lumo-Fresh</h1>
    <div class="brand__rule"></div>
    <p class="brand__tagline">Carpet &amp; Upholstery Cleaning</p>
  </header>

  <p class="area">Servicing Albury/<br>Wodonga and<br>surrounding areas</p>

  <div class="contact contact--phone">
    <svg class="contact__icon" width="34" height="34" viewBox="0 0 24 24" aria-hidden="true">
      <path d="M6.6 10.8a15.1 15.1 0 0 0 6.6 6.6l2.2-2.2a1 1 0 0 1 1-.25 11.4 11.4 0 0 0 3.6.57 1 1 0 0 1 1 1V20a1 1 0 0 1-1 1A17 17 0 0 1 3 4a1 1 0 0 1 1-1h3.5a1 1 0 0 1 1 1c0 1.25.2 2.45.57 3.57a1 1 0 0 1-.25 1z" fill="var(--white)"/>
    </svg>
    <span>Gus: 046 127 3904</span>
  </div>

  <div class="contact contact--email">
    <svg class="contact__icon" width="38" height="28" viewBox="0 0 38 28" aria-hidden="true">
      <rect x="1.5" y="1.5" width="35" height="25" fill="var(--blue)" stroke="var(--white)" stroke-width="3"/>
      <path d="M2 3 L19 16 L36 3" fill="none" stroke="var(--white)" stroke-width="3"/>
    </svg>
    <span>lumofresh1@tealpost.example</span>
  </div>
</main>
</body>
</html>
```